Martin Halvorsen Pianist Teacher Examiner

I need a website design to promote my business as a professional classical pianist and a piano teacher of all levels.
I want it to look a mixture of old world opulence (eg antique grand piano?) and modern text. It should have an elegant, beautiful and relaxing feel.

Industry/Entity Type

Teacher

```html
<!DOCTYPE html>
<html lang="en">
<head>
<meta charset="utf-8">
<title>Martin Halvorsen – Professional Piano Teacher</title>
<link rel="stylesheet" href="https://fonts.googleapis.com/css2?family=Cinzel:wght@400;500&family=Fondamento:ital@1&family=Open+Sans&family=Arimo&display=swap">
<style>
  :root {
    --sky: #00aeef;
    --sky-deep: #1a9fdc;
    --ink: #111111;
    --paper: #ffffff;
    --button-top: #ffffff;
    --button-bottom: #c9c9c9;
    --photo-dark: #2b2b2b;
    --photo-mid: #6a6a6a;
    --keys-dark: #1c1c1c;
    --keys-light: #d9d9d9;
  }
  * { margin: 0; padding: 0; box-sizing: border-box; }
  html, body {
    width: 1200px; height: 1000px; overflow: hidden;
    background: var(--paper); color: var(--ink);
  }
  .page { position: relative; width: 1200px; height: 1000px; }

  .top-band {
    position: absolute; left: 51px; top: 38px; width: 1093px; height: 34px;
    background: var(--sky);
  }

  .main-nav {
    position: absolute; left: 55px; top: 92px; width: 1088px;
    display: flex; justify-content: space-between;
    font-family: "Cinzel", serif; font-size: 29px; letter-spacing: 2px;
  }
  .main-nav a { color: var(--ink); text-decoration: none; text-transform: uppercase; }

  .hero {
    position: absolute; left: 51px; top: 150px; width: 1096px; height: 313px;
    background: linear-gradient(90deg, var(--sky) 0%, var(--sky-deep) 100%);
  }
  .hero-name {
    position: absolute; left: 77px; top: 45px;
    font-family: "Cinzel", serif; font-weight: 500; font-size: 54px; letter-spacing: 2px;
  }
  .hero-role {
    position: absolute; left: 54px; top: 142px;
    font-family: "Cinzel", serif; font-weight: 500; font-size: 42px; letter-spacing: 2px;
  }
  .enroll-button {
    position: absolute; left: 74px; top: 236px; width: 204px; height: 60px;
    border-radius: 9px;
    background: linear-gradient(90deg, var(--button-top) 40%, var(--button-bottom) 100%);
    display: flex; align-items: center; justify-content: center;
    font-family: "Arimo", Arial, sans-serif; font-size: 28px; color: var(--ink);
    text-decoration: none;
  }
  .portrait {
    position: absolute; right: 0; top: 0; width: 214px; height: 313px;
    background: radial-gradient(ellipse at 50% 40%, var(--photo-mid) 0%, var(--photo-dark) 75%);
  }

  .quote {
    position: absolute; left: 0; top: 552px; width: 1200px; text-align: center;
    font-family: "Fondamento", cursive; font-style: italic; font-size: 46px; line-height: 54px;
  }
  .quote-author {
    position: absolute; right: 62px; top: 696px;
    font-family: "Cinzel", serif; font-size: 36px; letter-spacing: 2px;
  }

  .keyboard-photo {
    position: absolute; left: 0; top: 797px; width: 1200px; height: 143px;
    background: linear-gradient(180deg, var(--keys-dark) 0%, var(--keys-dark) 45%, var(--keys-light) 70%, var(--keys-light) 92%, var(--keys-dark) 100%);
  }

  .site-footer {
    position: absolute; left: 65px; top: 954px;
    font-family: "Open Sans", Arial, sans-serif; font-size: 17px;
  }
</style>
</head>
<body>
<div class="page">
  <div class="top-band"></div>

  <nav class="main-nav">
    <a href="#">Home</a>
    <a href="#">Biography</a>
    <a href="#">Lessons</a>
    <a href="#">Students</a>
    <a href="#">Policy</a>
    <a href="#">Contact</a>
  </nav>

  <section class="hero">
    <h1 class="hero-name">Martin Halvorsen</h1>
    <p class="hero-role">Professional piano teacher</p>
    <a class="enroll-button" href="#">ENROLL</a>
    <div class="portrait" role="img" aria-label="Portrait photograph of the piano teacher"></div>
  </section>

  <blockquote class="quote">“Witout a piano I don’t know how to stand,<br>don’t know what to do with my hands.”</blockquote>
  <p class="quote-author">Lena Marsh</p>

  <div class="keyboard-photo" role="img" aria-label="Black and white photograph of an old piano keyboard"></div>

  <footer class="site-footer">©2014 Martin Halvorsen. All right reserved</footer>
</div>
</body>
</html>
```